Verpackungsdesign für hochwertigs Nahrungsergänzungmittel
Zielgruppe
Nahrungsergänzungsmittel aus hochwertigen Zutaten , werden in Deutschland gefertigt. Unsere Produkte sollen sowohl Jung als auch Alt ansprechen dabei modern und zugleich auch medizinisch Wirkung ausstrahlen und vertrauen erwecken da diese auch in der Apotheke verkauft werden.
kurzes Update zum Briefing:
Am Anfang ist eine Mischung aus verschiedenen Suppliments. Wir denken aber weiter und wollen ein Design das mehrere Suppliments abdeckt wie z.b. auch Kalium, Magnesium etc. von daher soll das Design alles abdecken, schlicht aber auch zugleich ansprechend und natürlich sein. Die Marke nennt sich LumaKor.
Es wird sowohl im Direktvertrieb, wie auch Online und in der Apotheke angeboten
Aufgabenstellung
Das Produkt soll Nachhaltigkeit suggerieren, sowie gute Qualität der Inhaltsstoffe. Das Produkt ist in einer Faltschachtel.

```html
<!DOCTYPE html>
<html lang="de">
<head>
<meta charset="utf-8">
<title>LumaKor – Verpackungsdesign Nahrungsergänzungsmittel</title>
<link rel="stylesheet" href="https://fonts.googleapis.com/css2?family=PT+Sans+Narrow&family=Open+Sans:wght@300;400&display=swap">
<style>
  :root {
    --green: #9fbd32;
    --green-dark: #7e9a22;
    --green-pale: #f6f9e7;
    --line-soft: #dfe8c4;
    --badge-edge: #d9c92a;
    --ink: #4a4a4a;
    --white: #ffffff;
    --swoosh-a: #3e6ea8;
    --swoosh-b: #9ab7c9;
    --flag-1: #2b2b2b;
    --flag-2: #d8262c;
    --flag-3: #f1c21b;
  }
  * { box-sizing: border-box; margin: 0; padding: 0; }
  html, body { width: 846px; height: 1200px; overflow: hidden; background: var(--white); }
  body { position: relative; font-family: "Open Sans", Arial, sans-serif; color: var(--ink); }

  .panel {
    position: absolute;
    background: var(--white);
    display: flex; flex-direction: column; align-items: center; justify-content: center;
    overflow: hidden;
  }
  .floral {
    position: absolute; left: 8%; right: 8%; top: 10%; bottom: 6%;
    border-radius: 50%;
    background: radial-gradient(ellipse at center, #e4edc6 0%, #eef3db 45%, rgba(255,255,255,0) 72%);
  }

  .brand-badge {
    position: relative; z-index: 1;
    width: 8.4em; height: 8.4em;
    background: var(--white);
    border: 0.22em solid var(--badge-edge);
    border-radius: 1em;
    display: flex; flex-direction: column; align-items: center; justify-content: center; gap: 0.6em;
    box-shadow: 0 0.2em 0.6em rgba(0,0,0,0.08);
  }
  .brand-mark { width: 2.6em; height: 2.6em; background: var(--green); border-radius: 0.3em; }
  .brand-name { font-family: "Open Sans", Arial, sans-serif; font-size: 1.6em; color: var(--ink); font-weight: 400; }

  .product-card {
    position: relative; z-index: 1;
    margin-top: 0.7em;
    width: 21em; height: 20em;
    background: var(--green);
    border-radius: 1.2em;
    box-shadow: 0 0 1.4em rgba(159,189,50,0.35);
    display: flex; flex-direction: column; align-items: center;
    padding-top: 2.2em;
    color: var(--white);
  }
  .product-name { font-family: "PT Sans Narrow", "Arial Narrow", sans-serif; font-size: 3.7em; line-height: 1; letter-spacing: 0.02em; }
  .swoosh { width: 12em; height: 1.4em; margin-top: 0.5em; }
  .product-type { font-size: 1.3em; font-weight: 300; margin-top: 0.6em; }
  .divider { width: 15.5em; height: 0.08em; background: rgba(255,255,255,0.8); margin-top: 0.5em; }
  .info-label { font-size: 0.75em; font-weight: 300; margin-top: 0.7em; }
  .icon-row { display: flex; gap: 2.2em; margin-top: 1.4em; }
  .icon { width: 2.9em; height: 2.9em; }

  .box-front { left: 60px; top: 40px; width: 310px; height: 360px; font-size: 9.6px; border: 1px solid var(--line-soft); border-top: 14px solid var(--green); }
  .flat-label { left: 380px; top: 402px; width: 428px; height: 322px; font-size: 10.6px; border: 2px solid var(--green); box-shadow: 0 0 14px rgba(159,189,50,0.45); }
  .jar-label { left: 72px; top: 742px; width: 272px; height: 335px; font-size: 7.8px; border: 1px solid var(--line-soft); }

  .wrap-stage { position: absolute; left: 352px; top: 752px; width: 494px; height: 352px; background: var(--green-pale); }
  .wrap-label { position: absolute; left: 18px; top: 140px; width: 458px; height: 160px; background: var(--white); font-size: 5.6px; }
  .wrap-label .center { position: absolute; left: 160px; top: 0; width: 138px; height: 160px; display: flex; flex-direction: column; align-items: center; justify-content: center; }
  .field { position: absolute; background: var(--green); border-radius: 5px; }
  .field-title { position: absolute; font-size: 6px; color: var(--ink); }
  .field-usage { left: 10px; top: 12px; width: 80px; height: 96px; }
  .field-maker { left: 10px; top: 112px; width: 80px; height: 40px; }
  .field-ingredients { left: 380px; top: 12px; width: 68px; height: 104px; }
  .net-weight { position: absolute; left: 100px; top: 140px; font-size: 7px; }
  .best-before { position: absolute; left: 380px; top: 128px; font-size: 5.6px; }
</style>
</head>
<body>

<svg width="0" height="0" style="position:absolute">
  <defs>
    <linearGradient id="swoosh-grad" x1="0" x2="1">
      <stop offset="0" stop-color="#ffffff" stop-opacity="0"/>
      <stop offset="0.35" stop-color="#3e6ea8"/>
      <stop offset="1" stop-color="#9ab7c9" stop-opacity="0.2"/>
    </linearGradient>
    <symbol id="swoosh" viewBox="0 0 120 14">
      <path d="M2 12 C40 2, 80 2, 118 8 C80 5, 40 6, 2 12 Z" fill="url(#swoosh-grad)"/>
    </symbol>
    <symbol id="icon-leaf" viewBox="0 0 30 30">
      <circle cx="15" cy="15" r="14" fill="#fff"/>
      <path d="M9 18 C9 11, 14 9, 16 9 C16 14, 13 18, 9 18 Z" fill="#9fbd32"/>
      <path d="M14 21 C14 14, 19 12, 22 12 C22 18, 18 21, 14 21 Z" fill="#9fbd32"/>
    </symbol>
    <symbol id="icon-flag" viewBox="0 0 30 30">
      <circle cx="15" cy="15" r="14" fill="#fff"/>
      <clipPath id="flag-clip"><circle cx="15" cy="15" r="8.5"/></clipPath>
      <g clip-path="url(#flag-clip)">
        <rect x="6" y="6" width="18" height="6" fill="#2b2b2b"/>
        <rect x="6" y="12" width="18" height="6" fill="#d8262c"/>
        <rect x="6" y="18" width="18" height="6" fill="#f1c21b"/>
      </g>
    </symbol>
    <symbol id="icon-info" viewBox="0 0 30 30">
      <circle cx="15" cy="15" r="14" fill="#fff"/>
      <circle cx="15" cy="9.5" r="1.6" fill="#9fbd32"/>
      <rect x="13.7" y="13" width="2.6" height="9" rx="1" fill="#9fbd32"/>
    </symbol>
  </defs>
</svg>

<!-- Faltschachtel, Vorderseite -->
<section class="panel box-front">
  <div class="floral" role="img" aria-label="Feine grüne Linienzeichnung von Blüten"></div>
  <div class="brand-badge"><span class="brand-mark"></span><span class="brand-name">LumaKor</span></div>
  <div class="product-card">
    <h1 class="product-name">NOXA NIGHT</h1>
    <svg class="swoosh"><use href="#swoosh"/></svg>
    <p class="product-type">Nahrungsergänzungsmittel</p>
    <span class="divider"></span>
    <p class="info-label">Informationen</p>
    <div class="icon-row">
      <svg class="icon"><use href="#icon-leaf"/></svg>
      <svg class="icon"><use href="#icon-flag"/></svg>
      <svg class="icon"><use href="#icon-info"/></svg>
    </div>
  </div>
</section>

<!-- Etikett Magnesium -->
<section class="panel flat-label">
  <div class="floral" role="img" aria-label="Feine grüne Linienzeichnung von Blüten"></div>
  <div class="brand-badge"><span class="brand-mark"></span><span class="brand-name">LumaKor</span></div>
  <div class="product-card">
    <h2 class="product-name">MAGNESIUM</h2>
    <svg class="swoosh"><use href="#swoosh"/></svg>
    <p class="product-type">Nahrungsergänzungsmittel</p>
    <span class="divider"></span>
    <p class="info-label">Informationen</p>
    <div class="icon-row">
      <svg class="icon"><use href="#icon-leaf"/></svg>
      <svg class="icon"><use href="#icon-flag"/></svg>
      <svg class="icon"><use href="#icon-info"/></svg>
    </div>
  </div>
</section>

<!-- Dosenetikett Noxa Night -->
<section class="panel jar-label">
  <div class="floral" role="img" aria-label="Feine grüne Linienzeichnung von Blüten"></div>
  <div class="brand-badge"><span class="brand-mark"></span><span class="brand-name">LumaKor</span></div>
  <div class="product-card">
    <h2 class="product-name">NOXA NIGHT</h2>
    <svg class="swoosh"><use href="#swoosh"/></svg>
    <p class="product-type">Nahrungsergänzungsmittel</p>
    <span class="divider"></span>
    <p class="info-label">Informationen</p>
    <div class="icon-row">
      <svg class="icon"><use href="#icon-leaf"/></svg>
      <svg class="icon"><use href="#icon-flag"/></svg>
      <svg class="icon"><use href="#icon-info"/></svg>
    </div>
  </div>
</section>

<!-- Rundumetikett Magnesium -->
<div class="wrap-stage">
  <section class="wrap-label">
    <span class="field-title" style="left:12px;top:2px">Verzehrempfehlung</span>
    <div class="field field-usage"></div>
    <div class="field field-maker"></div>
    <span class="field-title" style="left:14px;top:114px;color:#fff">Hersteller</span>
    <span class="net-weight">80g</span>
    <div class="center">
      <div class="floral" role="img" aria-label="Feine grüne Linienzeichnung von Blüten"></div>
      <div class="brand-badge"><span class="brand-mark"></span><span class="brand-name">LumaKor</span></div>
      <div class="product-card">
        <h2 class="product-name">MAGNESIUM</h2>
        <svg class="swoosh"><use href="#swoosh"/></svg>
        <p class="product-type">Nahrungsergänzungsmittel</p>
        <span class="divider"></span>
        <p class="info-label">Informationen</p>
        <div class="icon-row">
          <svg class="icon"><use href="#icon-leaf"/></svg>
          <svg class="icon"><use href="#icon-flag"/></svg>
          <svg class="icon"><use href="#icon-info"/></svg>
        </div>
      </div>
    </div>
    <span class="field-title" style="left:382px;top:2px">Zutaten</span>
    <div class="field field-ingredients"></div>
    <span class="best-before">Mindesthaltbar bis</span>
  </section>
</div>

</body>
</html>
```